Kettle Ledger Business Card design

We need a stand out business card design for Accounting practice based in Australia specialising in pubs, clubs and hotels. We help venues maximise margins, create time and manage cashflow. One club we have been working with for the last 6 months has increased revenue by 3% and margin by 5% in this time frame. We have a back office outsourced system that costs less than having a full time employee and also allows the venues the added benefit of:<br/>-using the office space to become a revenue generating opportunity. <br/>-a complete system to enhance governance, accountability and efficiency within their operation<br/>-52 weeks cover so no hassle to cover annual/sick .. leave<br/><br/>We would like to see designs that use the colours of our logo (green & blue).
Target Market(s)
Australian Pubs, Clubs & Hotels abookkeeping, accounting and tax services
Industry/Entity Type
Accountant
Contact Information for Business Card
Miriam Oakley CPA
Principal
Accountant Tax Agent
Miriam@KettleLedger-example.com.au
0418693142
www.kettleledger-example.com.au
Accounting / Payroll / Tax / SMSF / Technology
Colors
Designer to choose colors to be used in the design.
Look and feel
Each slider illustrates characteristics of the customer's brand and the style your logo design should communicate.

```html
<!DOCTYPE html>
<html lang="en">
<head>
<meta charset="utf-8">
<title>Kettle Ledger – Business Card</title>
<link rel="stylesheet" href="https://fonts.googleapis.com/css2?family=Archivo:wght@700;800&family=Questrial&display=swap">
<style>
  :root {
    --brand-blue: #24448e;
    --brand-green: #137640;
    --paper: #ffffff;
    --ink: #2e2e2e;
    --backdrop: #cccccc;
  }
  * { margin: 0; padding: 0; box-sizing: border-box; }
  html, body {
    width: 1200px; height: 1200px; overflow: hidden;
    background: var(--backdrop);
  }
  .sheet { position: relative; width: 1200px; height: 1200px; }

  /* ---------- front ---------- */
  .card-front {
    position: absolute; left: 102px; top: 52px;
    width: 1013px; height: 512px;
    box-shadow: 0 22px 26px -14px rgba(0,0,0,0.35);
  }
  .card-front .card-shape { position: absolute; inset: 0; width: 100%; height: 100%; }

  .front-brand {
    position: absolute; left: 92px; top: 241px;
    display: flex; align-items: center; gap: 12px;
  }
  .brand-dot {
    width: 30px; height: 30px; border-radius: 50%;
    background: var(--brand-green);
    flex: none;
  }
  .brand-name {
    font-family: "Archivo", Arial, sans-serif;
    font-weight: 800;
    color: var(--brand-blue);
    font-size: 31px;
    letter-spacing: -0.5px;
    white-space: nowrap;
  }

  .divider {
    position: absolute; left: 425px; top: 117px;
    width: 2px; height: 211px; background: var(--brand-blue);
  }

  .person { position: absolute; left: 461px; top: 110px; }
  .person-name {
    font-family: "Archivo", Arial, sans-serif;
    font-weight: 800; font-size: 36px; line-height: 1;
    color: var(--brand-blue); letter-spacing: -0.3px;
  }
  .person-role {
    font-family: "Questrial", "Century Gothic", sans-serif;
    font-size: 25px; line-height: 1.1; color: var(--ink);
    margin-top: 4px;
  }

  .contacts { position: absolute; left: 457px; top: 198px; list-style: none; }
  .contact {
    display: flex; align-items: center; height: 50px;
    font-family: "Questrial", "Century Gothic", sans-serif;
    font-size: 24px; color: var(--ink); white-space: nowrap;
  }
  .contact svg { width: 30px; height: 30px; flex: none; margin-right: 18px; }

  /* ---------- back ---------- */
  .card-back {
    position: absolute; left: 101px; top: 615px;
    width: 1014px; height: 512px;
    background: var(--brand-blue);
  }
  .back-brand {
    position: absolute; left: 0; right: 0; top: 218px;
    display: flex; justify-content: center; align-items: center; gap: 22px;
  }
  .back-brand .brand-dot { width: 62px; height: 62px; background: var(--paper); }
  .back-brand .brand-name { color: var(--paper); font-size: 66px; letter-spacing: -1px; }

  .services {
    position: absolute; left: 0; right: 0; top: 438px; height: 45px;
    background: var(--brand-green);
    display: flex; justify-content: center; align-items: center; gap: 26px;
    list-style: none;
    font-family: "Archivo", Arial, sans-serif; font-weight: 700;
    font-size: 29px; color: var(--paper);
  }
  .services .sep { font-weight: 700; }
</style>
</head>
<body>
<div class="sheet">

  <section class="card-front">
    <svg class="card-shape" viewBox="164 84 1632 824" preserveAspectRatio="none" aria-hidden="true">
      <rect x="164" y="84" width="1632" height="824" fill="var(--brand-blue)"/>
      <path fill="var(--paper)" d="M189,105 H1770 V732 C1650,760 1500,800 1300,808 C1150,815 1000,785 800,770 C600,755 400,770 189,822 Z"/>
      <path fill="var(--brand-green)" d="M189,775 C400,730 650,715 850,740 C1050,765 1150,790 1300,788 C1500,785 1650,740 1770,710 L1770,714 C1650,748 1500,790 1300,794 C1150,796 1050,776 850,762 C650,746 400,760 189,802 Z"/>
    </svg>

    <div class="front-brand">
      <span class="brand-dot"></span>
      <span class="brand-name">Kettle Ledger</span>
    </div>

    <div class="divider"></div>

    <div class="person">
      <h1 class="person-name">Miriam Oakley CPA</h1>
      <p class="person-role">Principal / Accountant Tax Agent</p>
    </div>

    <ul class="contacts">
      <li class="contact">
        <svg viewBox="0 0 24 24" aria-hidden="true"><path fill="none" stroke="var(--brand-blue)" stroke-width="1.8" stroke-linejoin="round" d="M17 3.5c2 0 3.5 1 3.5 2.3 0 .8-1.3 1.6-2.3 1.5l-1.7-.2c-1.2 0-2.8 1.5-4.2 3.5-1.5 2.2-2.3 4.4-1.8 5.4l.8 1.5c.4.9-.3 2.3-1 2.6-1.4.6-4.5-.8-4.3-3.5.3-4.4 5-12.6 11-13.1z"/></svg>
        0418693142
      </li>
      <li class="contact">
        <svg viewBox="0 0 24 24" aria-hidden="true"><rect x="2.5" y="5" width="19" height="14" fill="none" stroke="var(--brand-blue)" stroke-width="2.6"/><path d="M3 6l9 7 9-7" fill="none" stroke="var(--brand-blue)" stroke-width="2.6"/></svg>
        Miriam@KettleLedger-example.com.au
      </li>
      <li class="contact">
        <svg viewBox="0 0 24 24" aria-hidden="true"><circle cx="12" cy="13" r="9" fill="var(--brand-blue)"/><g fill="none" stroke="#fff" stroke-width="0.9"><ellipse cx="12" cy="13" rx="4" ry="9"/><line x1="12" y1="4" x2="12" y2="22"/><line x1="3" y1="13" x2="21" y2="13"/><line x1="4.5" y1="8.5" x2="19.5" y2="8.5"/><line x1="4.5" y1="17.5" x2="19.5" y2="17.5"/></g></svg>
        www.kettleledger-example.com.au
      </li>
    </ul>
  </section>

  <section class="card-back">
    <div class="back-brand">
      <span class="brand-dot"></span>
      <span class="brand-name">Kettle Ledger</span>
    </div>
    <ul class="services">
      <li>Accounting</li><li class="sep">-</li>
      <li>Payroll</li><li class="sep">-</li>
      <li>Tax</li><li class="sep">-</li>
      <li>SMSF</li><li class="sep">-</li>
      <li>Technology</li>
    </ul>
  </section>

</div>
</body>
</html>
```